Brightwave MolarNet IT Inc. new website

i need a website for my company which is dedicated to installation and service of computer systems in Dental Offices. I would like for it to encompass a technology feel and professional look. The company deals with all aspects of technology like, Audio Visual, computer systems and networks, Cloud services like data backup, data center. We provide manage services, support and services to Dental Professionals.
Updates

Looking for a Technology font but professional look Added Wednesday, April 20, 2016

Target Market(s)

Dental, Dentist

Industry/Entity Type

Dental

Number of Pages Required

5+ page

Font styles to use
Other font styles liked:
• Futuristic or Techy

Colors
0255a3
ec1f27

Requirements
Must have
• Tabs
Nice to have
• Have no idea maybe some suggestion on your part may help
Should not have
• A professional feel but have a techy look

Files

```html
<!DOCTYPE html>
<html lang="en">
<head>
<meta charset="utf-8">
<title>Brightwave MolarNet IT Inc.</title>
<link href="https://fonts.googleapis.com/css2?family=Roboto:wght@300;400;500;700&family=Roboto+Condensed:wght@700&display=swap" rel="stylesheet">
<style>
:root{
  --brand-blue:#0255a3;
  --nav-dark:#1d3f86;
  --brand-red:#ec1f27;
  --ink:#333;
  --hero-dark:#25272c;
  --footer:#24262b;
  --light:#f2f2f2;
  --white:#fff;
}
*{margin:0;padding:0;box-sizing:border-box}
html,body{width:1200px;height:2497px;overflow:hidden}
body{position:relative;background:var(--white);font-family:'Roboto',Arial,sans-serif;color:var(--ink)}
.abs{position:absolute}
/* header */
.brand{left:98px;top:40px;display:flex;align-items:center;gap:10px;font-size:25px;font-weight:700;color:var(--brand-blue)}
.brand-mark{width:20px;height:20px;background:var(--brand-blue)}
.search{left:605px;top:45px;width:272px;height:35px;border:1px solid #ddd;font-size:11px;color:#555;padding:11px 14px}
.search svg{position:absolute;right:12px;top:10px}
.question{left:880px;top:38px;width:172px;text-align:right;font-size:16px;color:#333;line-height:22px}
.question span{color:#7a9cc9;display:block}
.call{left:1066px;top:44px;width:34px;height:34px;border-radius:50%;background:#7f97c2}
/* nav */
.nav{left:0;top:125px;width:1200px;height:50px;background:linear-gradient(#0d68d0,#0450a8)}
.nav a{position:absolute;top:0;height:50px;line-height:50px;color:var(--white);font-size:13px;text-decoration:none;text-align:center;border-right:1px solid rgba(255,255,255,.15)}
.nav a.active{background:var(--nav-dark)}
/* hero */
.hero-bg{left:0;top:175px;width:1200px;height:460px}
.hero-frame{left:98px;top:208px;width:1003px;height:507px;background:var(--white);padding:8px}
.hero-img{width:100%;height:100%;
  background:
    radial-gradient(ellipse 22% 40% at 62% 30%, rgba(250,250,252,.85), rgba(250,250,252,0) 70%),
    radial-gradient(ellipse 26% 45% at 55% 78%, rgba(225,228,232,.9), rgba(225,228,232,0) 70%),
    radial-gradient(circle at 18% 25%, rgba(120,220,255,.35), rgba(120,220,255,0) 25%),
    radial-gradient(circle at 30% 55%, rgba(140,230,200,.25), rgba(140,230,200,0) 22%),
    linear-gradient(90deg,#1e2e44 0%,#3a5470 30%,#5d7690 60%,#3f5268 100%)}
.hero-title{left:708px;top:440px;font-family:'Roboto Condensed',Arial,sans-serif;font-size:40px;line-height:46px;color:var(--white);font-weight:700;text-shadow:0 1px 3px rgba(0,0,0,.3)}
.hero-sub{left:710px;top:540px;font-size:14px;line-height:20px;color:#eee;width:340px}
.arrow{width:34px;height:34px;border-radius:50%;background:#111}
/* services */
.sec-title{left:97px;top:770px;font-size:32px;font-weight:400;color:#222}
.sec-title b{font-weight:400;color:var(--brand-blue)}
.sec-intro{left:300px;top:772px;width:752px;padding-left:22px;border-left:1px solid #ddd;font-size:11.5px;line-height:20px;color:#444}
.card{width:310px;top:848px}
.card .ph{height:197px;border:4px solid #e6e6e6}
.card h3{font-size:18px;font-weight:400;color:#444;margin-top:22px}
.card p{font-size:11.5px;line-height:20px;color:#555;margin-top:10px;width:270px}
.card svg{position:absolute;right:6px;top:262px}
/* welcome */
.welcome{left:0;top:1203px;width:1200px;height:317px;
  background:
    linear-gradient(180deg,rgba(236,74,82,0) 55%,rgba(190,40,48,.55) 100%),
    radial-gradient(ellipse 8% 70% at 40% 100%, rgba(170,30,38,.45), rgba(170,30,38,0) 70%),
    radial-gradient(ellipse 6% 60% at 80% 100%, rgba(170,30,38,.4), rgba(170,30,38,0) 70%),
    linear-gradient(#ee4a53,#e43e47);
  text-align:center;color:var(--white)}
.welcome h2{font-size:32px;font-weight:400;margin-top:64px}
.welcome p{width:880px;margin:18px auto 0;font-size:11.5px;line-height:21px}
.welcome .btn{display:inline-block;margin-top:26px;width:158px;height:40px;line-height:38px;border:1px solid var(--white);font-size:14px;letter-spacing:1px}
/* features */
.feat{top:1588px;width:286px}
.feat .ic{width:62px;height:62px;background:var(--brand-blue);display:flex;align-items:center;justify-content:center}
.feat h3{font-size:20px;font-weight:400;color:#333;margin-top:28px}
.feat p{font-size:11.5px;line-height:21px;color:#555;margin-top:14px}
.feat .more{font-size:11px;color:var(--brand-blue);margin-top:18px;display:flex;align-items:center;gap:6px}
.feat .rule{height:2px;margin-top:22px}
/* news */
.news{left:0;top:1883px;width:1200px;height:452px;background:linear-gradient(160deg,#ececec,#f7f7f7 50%,#efefef)}
.news h2{position:absolute;top:48px;width:100%;text-align:center;font-size:30px;font-weight:400;color:#333}
.post{top:2042px;width:245px;height:220px}
.post .pic{position:absolute;inset:0}
.post .cap{position:absolute;left:20px;top:142px;background:var(--white);font-size:15px;color:#444;padding:7px 10px}
.post .date{position:absolute;left:20px;top:178px;background:var(--brand-blue);color:var(--white);font-size:12px;padding:8px 10px}
/* footer */
.footer{left:0;top:2335px;width:1200px;height:162px;background:var(--footer);color:var(--white)}
.soc{top:50px;width:24px;height:24px;border-radius:50%;background:var(--white)}
.fi{top:36px;width:34px;height:34px;border-radius:50%;border:1px solid #aaa;display:flex;align-items:center;justify-content:center}
.ft{top:38px;font-size:13px;line-height:19px}
.copy{top:120px;width:100%;text-align:center;font-size:12px}
</style>
</head>
<body>

<header>
  <div class="abs brand"><span class="brand-mark"></span>Brightwave MolarNet IT</div>
  <div class="abs search">Search
    <svg width="14" height="14" viewBox="0 0 14 14"><circle cx="6" cy="6" r="4.5" fill="none" stroke="#333" stroke-width="1.6"/><line x1="9.5" y1="9.5" x2="13" y2="13" stroke="#333" stroke-width="1.8"/></svg>
  </div>
  <div class="abs question">Have any Question?<span>+1 555 0142 7700</span></div>
  <div class="abs call">
    <svg width="34" height="34" viewBox="0 0 34 34"><path d="M13 11c1 0 2 3 2 4s-1 1-1 2 2 3 3 3 1-1 2-1 4 1 4 2-2 3-4 3c-4 0-9-5-9-9 0-2 2-4 3-4z" fill="#fff"/></svg>
  </div>
</header>

<nav class="abs nav">
  <a class="active" style="left:98px;width:106px">HOME</a>
  <a style="left:204px;width:210px">ABOUT BRIGHTWAVE</a>
  <a style="left:414px;width:162px">OUR SERVICES</a>
  <a style="left:576px;width:148px">TECHNOLOGY</a>
  <a style="left:724px;width:100px">NEWS</a>
  <a style="left:824px;width:154px;border-right:none">CONTACT US</a>
</nav>

<section class="hero">
  <svg class="abs hero-bg" width="1200" height="460" viewBox="0 0 1200 460"><defs><linearGradient id="heroShade" x1="0" y1="0" x2="0" y2="1"><stop offset="0" stop-color="#2c2e33"/><stop offset="1" stop-color="#1f2125"/></linearGradient></defs><polygon points="0,0 1200,0 1200,380 0,460" fill="url(#heroShade)"/></svg>
  <div class="abs hero-frame"><div class="hero-img" role="img" aria-label="Technician with a laptop in a server room"></div></div>
  <div class="abs hero-title">CLOUD SERVICES<br>OF DATA BACKUP</div>
  <div class="abs hero-sub">Lorem ipsum dolor sit amet, consectetur adipisc sed do eiusmod tempor incididunt ut</div>
  <div class="abs arrow" style="left:30px;top:432px"><svg width="34" height="34"><polyline points="20,11 14,17 20,23" fill="none" stroke="#ccc" stroke-width="2"/></svg></div>
  <div class="abs arrow" style="left:1135px;top:432px"><svg width="34" height="34"><polyline points="14,11 20,17 14,23" fill="none" stroke="#ccc" stroke-width="2"/></svg></div>
</section>

<section class="services">
  <h2 class="abs sec-title"><b>Our</b> Services</h2>
  <p class="abs sec-intro">Lorem ipsum dolor sit amet, consectetur adipiscing elit, sed do eiusmod tempor incididunt ut labore et dolore magna aliqua. Ut enim ad minim veniam, quis nostrud exercitation ullamco laboris nisi ut aliquip ex ea commodo</p>
  <div class="abs card" style="left:98px">
    <div class="ph" role="img" aria-label="Audio visual presentation setup with laptop" style="background:radial-gradient(ellipse 30% 35% at 60% 45%, rgba(235,240,250,.8), rgba(235,240,250,0) 70%),linear-gradient(180deg,#4a4036 0%,#7a5e3a 40%,#c08a38 70%,#8a6430 100%)"></div>
    <h3>Audio Visual</h3>
    <p>Lorem ipsum dolor sit amet, consectetur ading elit, sed do eiusmod tempor incididunt</p>
    <svg width="10" height="16"><polyline points="2,2 8,8 2,14" fill="none" stroke="#999" stroke-width="1.5"/></svg>
  </div>
  <div class="abs card" style="left:446px">
    <div class="ph" role="img" aria-label="Cloud connected to a network of computers" style="background:radial-gradient(ellipse 28% 30% at 50% 30%, rgba(240,248,255,.9), rgba(240,248,255,0) 70%),linear-gradient(180deg,#5e9fd0 0%,#a9d2ef 45%,#dfeef8 70%,#7fb6de 100%)"></div>
    <h3>Computer systems and networks</h3>
    <p>Lorem ipsum dolor sit amet, consectetur ading elit, sed do eiusmod tempor incididunt</p>
    <svg width="10" height="16"><polyline points="2,2 8,8 2,14" fill="none" stroke="#999" stroke-width="1.5"/></svg>
  </div>
  <div class="abs card" style="left:793px">
    <div class="ph" role="img" aria-label="Hand holding a tablet with cloud backup graphics" style="background:radial-gradient(ellipse 25% 25% at 48% 42%, rgba(210,225,240,.75), rgba(210,225,240,0) 70%),radial-gradient(circle at 80% 30%, rgba(120,220,120,.35), rgba(120,220,120,0) 18%),linear-gradient(90deg,#5a7088 0%,#2c3a4a 45%,#1a222c 100%)"></div>
    <h3>Cloud services of data backup</h3>
    <p>Lorem ipsum dolor sit amet, consectetur ading elit, sed do eiusmod tempor incididunt</p>
    <svg width="10" height="16"><polyline points="2,2 8,8 2,14" fill="none" stroke="#999" stroke-width="1.5"/></svg>
  </div>
</section>

<section class="abs welcome" role="img" aria-label="Red tinted city skyline">
  <h2>WELCOME TO BRIGHTWAVE MOLARNET</h2>
  <p>Lorem ipsum dolor sit amet, consectetur adipiscing elit, sed do eiusmod tempor incididunt ut labore et dolore magna aliqua. Ut enim ad minim veniam, quis nostrud exercitation ullamco laboris nisi ut aliquip ex ea commodo consequat. Duis aute irure dolor in reprehenderit in voluptate velit esse cillum dolore eu fugiat nulla pariatur. Excepteur sint occaecat cupidatat non proident, sunt in culpa qui officia deserunt mollit anim id est laborum</p>
  <span class="btn">MORE INFO</span>
</section>

<section class="features">
  <div class="abs feat" style="left:98px">
    <div class="ic"><svg width="30" height="30" viewBox="0 0 30 30"><circle cx="12" cy="17" r="6" fill="none" stroke="#fff" stroke-width="3" stroke-dasharray="3 2"/><circle cx="12" cy="17" r="2" fill="#fff"/><circle cx="22" cy="8" r="4" fill="none" stroke="#fff" stroke-width="2.5" stroke-dasharray="2 2"/></svg></div>
    <h3>Manage Services</h3>
    <p>Lorem ipsum dolor sit amet, consectetur adipiscing elit, sed do eiusmod tempor incididunt ut labore et dolore magna aliqua. Ut enim ad minim veniam, quis</p>
    <div class="more">CLICK HERE <svg width="10" height="10"><circle cx="5" cy="5" r="5" fill="var(--brand-blue)"/><polyline points="4,3 6,5 4,7" fill="none" stroke="#fff" stroke-width="1.3"/></svg></div>
    <div class="rule" style="background:#9cc0e6"></div>
  </div>
  <div class="abs feat" style="left:456px">
    <div class="ic"><svg width="30" height="30" viewBox="0 0 30 30"><circle cx="15" cy="15" r="11" fill="none" stroke="#fff" stroke-width="3"/><circle cx="15" cy="15" r="5" fill="none" stroke="#fff" stroke-width="2.5"/></svg></div>
    <h3>Support and Service</h3>
    <p>Lorem ipsum dolor sit amet, consectetur adipiscing elit, sed do eiusmod tempor incididunt ut labore et dolore magna aliqua. Ut enim ad minim veniam, quis</p>
    <div class="more">CLICK HERE <svg width="10" height="10"><circle cx="5" cy="5" r="5" fill="var(--brand-blue)"/><polyline points="4,3 6,5 4,7" fill="none" stroke="#fff" stroke-width="1.3"/></svg></div>
    <div class="rule" style="background:#d9d9a8"></div>
  </div>
  <div class="abs feat" style="left:814px">
    <div class="ic"><svg width="30" height="30" viewBox="0 0 30 30"><circle cx="15" cy="15" r="12" fill="none" stroke="#fff" stroke-width="2"/><path d="M9 10c2-2 4-1 6 0 2-1 4-2 6 0 1 3-1 6-2 10-1 1-2-3-4-3s-3 4-4 3c-1-4-3-7-2-10z" fill="none" stroke="#fff" stroke-width="1.6"/></svg></div>
    <h3>Dental Professionals</h3>
    <p>Lorem ipsum dolor sit amet, consectetur adipiscing elit, sed do eiusmod tempor incididunt ut labore et dolore magna aliqua. Ut enim ad minim veniam, quis</p>
    <div class="more">CLICK HERE <svg width="10" height="10"><circle cx="5" cy="5" r="5" fill="var(--brand-blue)"/><polyline points="4,3 6,5 4,7" fill="none" stroke="#fff" stroke-width="1.3"/></svg></div>
    <div class="rule" style="background:#7f97c2"></div>
  </div>
</section>

<section class="abs news"><h2>LATEST NEWS</h2></section>
<article class="abs post" style="left:98px">
  <div class="pic" role="img" aria-label="Dentist with a young patient" style="background:radial-gradient(ellipse 35% 40% at 30% 30%, rgba(240,232,220,.8), rgba(240,232,220,0) 70%),linear-gradient(135deg,#d8cdbf 0%,#a89684 50%,#4e5a66 100%)"></div>
  <span class="cap">Sed ut perspiciatis unde</span><span class="date">13 AUG 2016</span></article>
<article class="abs post" style="left:351px">
  <div class="pic" role="img" aria-label="Woman in an office" style="background:radial-gradient(ellipse 30% 45% at 50% 40%, rgba(230,210,190,.7), rgba(230,210,190,0) 70%),linear-gradient(90deg,#8a6a44 0%,#c8a070 50%,#3a4656 100%)"></div>
  <span class="cap">Sed ut perspiciatis unde</span><span class="date">13 AUG 2016</span></article>
<article class="abs post" style="left:605px">
  <div class="pic" role="img" aria-label="Smiling woman portrait" style="background:radial-gradient(ellipse 40% 50% at 55% 50%, rgba(225,180,160,.9), rgba(225,180,160,0) 75%),linear-gradient(90deg,#4d7a82 0%,#8eaab0 60%,#3a4a50 100%)"></div>
  <span class="cap">Sed ut perspiciatis unde</span><span class="date">13 AUG 2016</span></article>
<article class="abs post" style="left:858px">
  <div class="pic" role="img" aria-label="Businessman under an umbrella" style="background:radial-gradient(ellipse 40% 25% at 45% 15%, rgba(15,20,28,.9), rgba(15,20,28,0) 80%),radial-gradient(circle at 70% 60%, rgba(240,150,40,.6), rgba(240,150,40,0) 15%),linear-gradient(180deg,#1e3450 0%,#6a90b0 60%,#3a5670 100%)"></div>
  <span class="cap">Sed ut perspiciatis unde</span><span class="date">13 AUG 2016</span></article>

<footer class="abs footer">
  <span class="abs soc" style="left:108px"></span>
  <span class="abs soc" style="left:143px"></span>
  <span class="abs soc" style="left:178px"></span>
  <span class="abs soc" style="left:213px"></span>

  <span class="abs fi" style="left:335px"><svg width="14" height="16" viewBox="0 0 14 16"><path d="M7 1a5 5 0 0 1 5 5c0 4-5 9-5 9S2 10 2 6a5 5 0 0 1 5-5z" fill="#fff"/><circle cx="7" cy="6" r="2" fill="var(--footer)"/></svg></span>
  <div class="abs ft" style="left:383px">18 Harbour Row, Kestrel Bay, 4021<br>Western Australia</div>

  <span class="abs fi" style="left:651px"><svg width="18" height="18" viewBox="6 8 20 20"><path d="M13 11c1 0 2 3 2 4s-1 1-1 2 2 3 3 3 1-1 2-1 4 1 4 2-2 3-4 3c-4 0-9-5-9-9 0-2 2-4 3-4z" fill="#fff"/></svg></span>
  <div class="abs ft" style="left:700px">Phone :<br><b>+1 555 0199 3021</b></div>

  <span class="abs fi" style="left:883px"><svg width="16" height="12" viewBox="0 0 16 12"><rect x="1" y="1" width="14" height="10" fill="none" stroke="#fff" stroke-width="1.5"/><polyline points="1,1 8,7 15,1" fill="none" stroke="#fff" stroke-width="1.5"/></svg></span>
  <div class="abs ft" style="left:932px">E-mail:<br>info@brightwavemolarnet.com</div>

  <div class="abs copy">© Copyright 2016 Brightwave MolarNet IT Inc. All Rights Reserved.</div>
</footer>

</body>
</html>
```